Book cover for a book about how to support a friend in grief.

The title of the book is "Quiet Hands on Heavy Days: Standing Beside Someone Across Hard Seasons" by Daniel P. Hartwig. I am a grief counselor and am passionate about educating people on how to better support someone in grief. I'd like the cover to tell a story. Maybe a person in grief and a friend standing near who doesn't know what to say. The image should appeal to all genders. I am open to ANY other ideas for the cover. Grief is a heavy topic but I don't want the cover to feel sad. It should convey hope.

```html
<!DOCTYPE html>
<html lang="en">
<head>
<meta charset="utf-8">
<title>Quiet Hands on Heavy Days — Book Cover</title>
<link rel="stylesheet" href="https://fonts.googleapis.com/css2?family=IM+Fell+English+SC&family=Montserrat:wght@500&display=swap">
<style>
  :root {
    --page: #ffffff;
    --cover: #0a1c27;
    --ink: #ffffff;
    --accent: #e8060c;
    --rule: #c0161a;
    --photo-light: rgba(118, 112, 104, 0.8);
    --photo-mid: rgba(58, 70, 80, 0.55);
    --photo-fade: rgba(10, 28, 39, 0);
    --stair-line: rgba(60, 78, 90, 0.18);
  }
  html, body {
    margin: 0;
    padding: 0;
    width: 1200px;
    height: 1200px;
    overflow: hidden;
    background: var(--page);
  }
  .cover {
    position: absolute;
    left: 247px;
    top: 71px;
    width: 703px;
    height: 1055px;
    background: var(--cover);
    overflow: hidden;
  }
  .cover-photo {
    position: absolute;
    left: 0;
    top: 0;
    width: 703px;
    height: 540px;
    background:
      radial-gradient(ellipse 300px 340px at 220px 160px, var(--photo-light) 0%, var(--photo-mid) 45%, var(--photo-fade) 100%),
      radial-gradient(ellipse 260px 260px at 560px 200px, var(--stair-line) 0%, var(--photo-fade) 100%);
  }
  .title {
    position: absolute;
    right: 84px;
    top: 402px;
    margin: 0;
    font-family: "IM Fell English SC", serif;
    font-weight: 400;
    font-size: 102px;
    line-height: 94px;
    text-align: right;
    color: var(--ink);
    letter-spacing: 1px;
  }
  .title span { display: block; }
  .title .title-accent { color: var(--accent); }
  .subtitle {
    position: absolute;
    left: 98px;
    top: 755px;
    width: 514px;
    margin: 0;
    padding: 12px 0;
    border-top: 2px solid var(--rule);
    border-bottom: 2px solid var(--rule);
    font-family: "Montserrat", sans-serif;
    font-weight: 500;
    font-size: 26px;
    line-height: 34px;
    text-align: center;
    color: var(--ink);
  }
  .author {
    position: absolute;
    left: 0;
    width: 100%;
    top: 962px;
    margin: 0;
    font-family: "Montserrat", sans-serif;
    font-weight: 500;
    font-size: 40px;
    line-height: 1;
    text-align: center;
    color: var(--ink);
    letter-spacing: 0.5px;
  }
</style>
</head>
<body>
  <section class="cover">
    <div class="cover-photo" role="img" aria-label="Photograph of a man seated on dark stairs, head bowed, hands clasped"></div>
    <h1 class="title">
      <span>Quiet Hands</span>
      <span>on Heavy</span>
      <span class="title-accent">Days</span>
    </h1>
    <p class="subtitle">Standing Beside Someone<br>Across Hard Seasons</p>
    <p class="author">Daniel P. Hartwig</p>
  </section>
</body>
</html>
```